New Dental Office Needs an Attractive and user friendly Website Designed

I need a website for a new dental office. The Name is Maplecrest Dentistry. I would like a Modern design with a user friendly interface and usability.
I would like a landing page, a page that lists the services we offer: Cosmetic Dentistry, Implants, Dental Hygiene, Emergency Services, Restorations, Dentures
Target Market(s)
Mid to upper class
Industry/Entity Type
Dentistry
Coding
Coded - Design and coding required
Number of Pages Required
1 page
Requirements
Must have
- Landing page that has a scheduling option, Procedures, operating hours, and contact us info
Nice to have
- Appealing design, Soft comforting colors. Easy to navigate page, Modern and professional.

```html
<!DOCTYPE html>
<html lang="en">
<head>
<meta charset="utf-8">
<title>Maplecrest Dentistry</title>
<link href="https://fonts.googleapis.com/css2?family=Lexend:wght@300;400;500;600;700&family=Montserrat:wght@400;500;600;700&display=swap" rel="stylesheet">
<style>
:root{
  --teal:#33d1bf;
  --teal-dark:#22b5a4;
  --navy:#0c2546;
  --ink:#1b2430;
  --mint:#eef8f5;
  --soft:#f4f6f8;
  --band:#22396b;
  --footer:#263545;
  --footer-dark:#1f2b38;
  --line:#e4ece9;
  --white:#fff;
}
*{box-sizing:border-box;margin:0;padding:0}
html,body{width:1200px;height:3150px;overflow:hidden}
body{position:relative;font-family:"Montserrat",sans-serif;color:var(--ink);background:var(--white)}
.abs{position:absolute}
h1,h2,h3,h4,.brand{font-family:"Lexend",sans-serif}

/* header */
.topbar{position:absolute;left:0;top:0;width:1200px;height:85px;border-top:3px solid #333;border-bottom:1px solid var(--line)}
.brand{position:absolute;left:164px;top:26px;font-size:28px;font-weight:500;color:var(--navy);letter-spacing:.3px}
.info{position:absolute;top:30px;display:flex;gap:10px;align-items:flex-start}
.info svg{width:22px;height:22px;margin-top:3px}
.info b{display:block;font-size:10px;font-weight:700;color:var(--navy)}
.info span{font-size:10px;color:#8a96a3}
.info .hl{color:var(--teal)}
.divider-v{position:absolute;left:614px;top:28px;width:1px;height:32px;background:var(--line)}
.btn{display:inline-block;background:var(--teal);color:#fff;font-weight:600;font-size:13px;border-radius:4px;text-align:center;font-family:"Montserrat",sans-serif}
.top-btn{position:absolute;left:899px;top:27px;width:139px;height:34px;line-height:34px}
.nav{position:absolute;left:0;top:85px;width:1200px;height:47px;border-bottom:1px solid var(--line)}
.nav a{position:absolute;top:16px;font-size:13px;font-weight:600;color:var(--navy);text-decoration:none}
.nav a.active{color:var(--teal)}
.nav .caret{position:absolute;left:416px;top:18px;width:9px;height:9px}
.nav .sep{position:absolute;left:899px;top:0;width:1px;height:47px;background:var(--line)}
.social{position:absolute;left:911px;top:18px;display:flex;gap:15px}
.social i{display:block;width:11px;height:11px;border-radius:50%;background:var(--navy)}

/* hero */
.hero{position:absolute;left:0;top:132px;width:1200px;height:575px;background:
  radial-gradient(ellipse 420px 380px at 870px 330px,#b8a9cf 0%,rgba(184,169,207,0) 100%),
  radial-gradient(ellipse 380px 520px at 520px 260px,#3f5fae 0%,rgba(63,95,174,0) 100%),
  linear-gradient(100deg,#b7bcc6 0%,#9fa6b6 25%,#6f80b4 45%,#9a98cc 70%,#a8a4d4 100%)}
.hero-shade{position:absolute;inset:0;background:linear-gradient(90deg,rgba(25,32,50,.45) 0%,rgba(25,32,50,.25) 50%,rgba(0,0,0,0) 75%)}
.tagline{position:absolute;left:164px;top:142px;display:flex;align-items:center;gap:6px;color:#fff;font-size:18px;font-family:"Lexend",sans-serif;font-weight:400}
.tagline i{display:block;width:65px;height:2px;background:var(--teal)}
.hero h1{position:absolute;left:164px;top:176px;font-size:46px;line-height:46px;font-weight:700;color:#fff}
.hero h1 em{font-style:normal;color:var(--teal)}
.hero p{position:absolute;left:164px;top:295px;width:540px;font-size:19px;line-height:23px;color:#fff;font-family:"Lexend",sans-serif;font-weight:300}
.hero-btn{position:absolute;left:164px;top:394px;width:139px;height:36px;line-height:36px}

/* sections */
.section-title{position:absolute;left:0;width:1200px;text-align:center;font-size:29px;font-weight:600;color:var(--navy)}
.section-sub{position:absolute;left:300px;width:600px;text-align:center;font-size:14px;line-height:18px;font-weight:500;color:#111}

.services{position:absolute;left:0;top:707px;width:1200px;height:789px;background:var(--mint)}
.svc-grid{position:absolute;left:163px;top:189px;width:875px;height:515px;display:grid;grid-template-columns:1fr 1fr;grid-template-rows:repeat(3,1fr);gap:2px;background:var(--line);box-shadow:0 6px 20px rgba(0,0,0,.05)}
.svc{background:#fff;position:relative}
.svc-icon{position:absolute;left:28px;top:50px;width:72px;height:72px;border-radius:50%;background:linear-gradient(135deg,#d7f5f0,#b9ece4)}
.svc h3{position:absolute;left:127px;top:42px;font-size:19px;font-weight:500;color:var(--navy)}
.svc p{position:absolute;left:127px;top:80px;width:285px;font-size:12.5px;line-height:18px;color:#222}

.team{position:absolute;left:0;top:1496px;width:1200px;height:532px}
.team-deco{position:absolute;left:0;top:135px;width:90px;height:170px;background:radial-gradient(circle at 40% 50%,rgba(51,209,191,.15),rgba(255,255,255,0) 70%)}
.cards{position:absolute;left:181px;top:172px;display:flex;gap:16px}
.doc{width:198px;height:292px;border:1px solid #eceff1;background:#fff;position:relative}
.doc-photo{width:198px;height:198px;background:linear-gradient(180deg,#d8f2ec 0%,#eef7f6 60%,#dfe6ee 100%)}
.doc .badge{position:absolute;left:85px;top:184px;width:28px;height:28px;border-radius:50%;background:var(--teal);border:2px solid #fff;display:flex;align-items:center;justify-content:center}
.doc h4{position:absolute;top:231px;width:100%;text-align:center;font-size:18px;font-weight:500;color:var(--ink)}
.doc span{position:absolute;top:257px;width:100%;text-align:center;font-size:10px;font-style:italic;font-weight:500}

.news{position:absolute;left:0;top:2028px;width:1200px;height:540px;background:var(--soft)}
.posts{position:absolute;left:183px;top:175px;display:flex;gap:15px}
.post{width:270px;height:298px;background:#fff;position:relative}
.post-img{width:270px;height:166px}
.date{position:absolute;left:0;top:122px;width:48px;height:44px;background:var(--band);color:#fff;text-align:center;font-family:"Lexend",sans-serif}
.date b{display:block;font-size:20px;line-height:24px;margin-top:3px;font-weight:600}
.date small{display:block;font-size:10px;line-height:12px}
.meta{position:absolute;left:30px;top:198px;display:flex;gap:22px;font-size:9.5px;color:#444}
.meta span{display:flex;gap:6px;align-items:center}
.post h4{position:absolute;left:30px;top:222px;width:220px;font-size:15.5px;line-height:18px;font-weight:500;color:var(--navy)}

.cta{position:absolute;left:0;top:2568px;width:1200px;height:119px;background:var(--band)}
.cta h3{position:absolute;left:187px;top:46px;font-size:21px;font-weight:400;color:#fff;letter-spacing:0}
.cta-btn{position:absolute;left:552px;top:42px;width:139px;height:35px;line-height:35px}
.cta .call{position:absolute;right:185px;top:44px;font-size:22px;font-weight:500;color:#fff;font-family:"Lexend",sans-serif}

.footer{position:absolute;left:0;top:2687px;width:1200px;height:407px;background:var(--footer);color:#dfe5ea}
.col{position:absolute;top:60px;width:263px}
.col h4{font-size:15px;font-weight:600;color:#fff;padding-bottom:14px;border-bottom:1px solid rgba(255,255,255,.12)}
.contact-row{display:flex;align-items:center;gap:10px;font-size:10px;height:33px;border-bottom:1px solid rgba(255,255,255,.08)}
.contact-row:last-child{border-bottom:0}
.contact-row svg{width:12px;height:12px}
.foot-social{display:flex;gap:7px;margin-top:36px;margin-left:2px}
.foot-social i{display:block;width:30px;height:30px;background:var(--teal)}
.svc-list{list-style:none;margin-top:16px}
.svc-list li{font-size:10.5px;height:27px;display:flex;align-items:center;gap:6px}
.svc-list li::before{content:"›";color:var(--teal);font-size:14px}
.hours .contact-row{justify-content:space-between;height:33px}
.hours .contact-row span{display:flex;gap:10px;align-items:center}
.copy{position:absolute;left:0;top:3094px;width:1200px;height:56px;background:var(--footer-dark);text-align:center;line-height:56px;font-size:9px;color:#6d7b89}
.totop{position:absolute;left:1159px;top:3104px;width:36px;height:36px;border-radius:50%;background:#111;display:flex;align-items:center;justify-content:center}
</style>
</head>
<body>

<header class="topbar">
  <div class="brand">Maplecrest Dentistry</div>
  <div class="info" style="left:493px">
    <svg viewBox="0 0 24 24" fill="none" stroke="#33d1bf" stroke-width="1.6"><path d="M5 3h4l2 5-3 2a11 11 0 0 0 6 6l2-3 5 2v4a2 2 0 0 1-2 2A17 17 0 0 1 3 5a2 2 0 0 1 2-2z"/></svg>
    <div><b>CALL US</b><span class="hl">+1 555 010 2048</span></div>
  </div>
  <div class="divider-v"></div>
  <div class="info" style="left:637px">
    <svg viewBox="0 0 24 24" fill="none" stroke="#33d1bf" stroke-width="1.6"><circle cx="12" cy="13" r="8"/><path d="M12 9v4l3 2M4 5l3-2M20 5l-3-2"/></svg>
    <div><b>OPENING HOURS</b><span>Mon-Sat: 9:00 A.M - 5:00 PM Sun Closed</span></div>
  </div>
  <a class="btn top-btn">SCHEDULE NOW</a>
</header>

<nav class="nav">
  <a class="active" style="left:164px">HOME</a>
  <a style="left:245px">ABOUT</a>
  <a style="left:333px">SERVICES</a>
  <svg class="caret" viewBox="0 0 10 10" fill="none" stroke="#8a96a3" stroke-width="1.3"><path d="M2 3l3 3 3-3"/></svg>
  <a style="left:438px">NEWS</a>
  <a style="left:519px">CONTACT</a>
  <div class="sep"></div>
  <div class="social"><i></i><i></i><i></i><i></i></div>
</nav>

<section class="hero">
  <div class="abs" style="inset:0" role="img" aria-label="Photo of a young girl in a dental chair having her teeth checked by a dentist in blue gloves"></div>
  <div class="hero-shade"></div>
  <div class="tagline"><i></i>Changing Lives One Smile at a Time</div>
  <h1>Dental Services for the<br><em>Entire Family</em></h1>
  <p>Donec quam felis, ultricies nec, pellentesque eu, pretium quis, sem. Nulla consequat massa quis enim. Donec pede justo, fringilla vel, aliquet nec.</p>
  <a class="btn hero-btn">LEARN MORE</a>
</section>

<section class="services">
  <h2 class="section-title" style="top:70px">Quick Services in Maplecrest Dentistry</h2>
  <p class="section-sub" style="top:113px">Donec quam felis, ultricies nec, pellentesque eu, pretium quis, sem. Nulla consequat massa quis enim. Donec pede justo, fringilla vel, aliquet nec.</p>
  <div class="svc-grid">
    <div class="svc"><div class="svc-icon" role="img" aria-label="Cosmetic dentistry line icon"></div><h3>Cosmetic Dentistry</h3><p>Our exceptional and experienced staff is dedicated to improving our patients’ dental health and enhancing smiles.</p></div>
    <div class="svc"><div class="svc-icon" role="img" aria-label="Dental implant line icon"></div><h3>Implants</h3><p>Our exceptional and experienced staff is dedicated to improving our patients’ dental health and enhancing smiles.</p></div>
    <div class="svc"><div class="svc-icon" role="img" aria-label="Dental hygiene line icon"></div><h3>Dental Hygiene</h3><p>Our exceptional and experienced staff is dedicated to improving our patients’ dental health and enhancing smiles.</p></div>
    <div class="svc"><div class="svc-icon" role="img" aria-label="Emergency first aid kit line icon"></div><h3>Emergency Services</h3><p>Our exceptional and experienced staff is dedicated to improving our patients’ dental health and enhancing smiles.</p></div>
    <div class="svc"><div class="svc-icon" role="img" aria-label="Tooth restoration line icon"></div><h3>Restorations</h3><p>Our exceptional and experienced staff is dedicated to improving our patients’ dental health and enhancing smiles.</p></div>
    <div class="svc"><div class="svc-icon" role="img" aria-label="Dentures line icon"></div><h3>Dentures</h3><p>Our exceptional and experienced staff is dedicated to improving our patients’ dental health and enhancing smiles.</p></div>
  </div>
</section>

<section class="team">
  <div class="team-deco" role="img" aria-label="Faint molecular pattern decoration"></div>
  <h2 class="section-title" style="top:60px">Meet Our Specialist</h2>
  <p class="section-sub" style="top:103px">Donec quam felis, ultricies nec, pellentesque eu, pretium quis, sem. Nulla consequat massa quis enim. Donec pede justo, fringilla vel, aliquet nec.</p>
  <div class="cards">
    <div class="doc"><div class="doc-photo" role="img" aria-label="Portrait of a dentist in a white coat"></div><div class="badge"><svg width="12" height="12" viewBox="0 0 24 24" fill="#fff"><path d="M12 21s-8-5-8-11a4.5 4.5 0 0 1 8-3 4.5 4.5 0 0 1 8 3c0 6-8 11-8 11z"/></svg></div><h4>Owen Hale</h4><span>Dental</span></div>
    <div class="doc"><div class="doc-photo" role="img" aria-label="Portrait of a neurologist in a white coat"></div><div class="badge"><svg width="12" height="12" viewBox="0 0 24 24" fill="#fff"><path d="M12 21s-8-5-8-11a4.5 4.5 0 0 1 8-3 4.5 4.5 0 0 1 8 3c0 6-8 11-8 11z"/></svg></div><h4>Martin Cole</h4><span>Neurology</span></div>
    <div class="doc"><div class="doc-photo" role="img" aria-label="Portrait of a neurologist with a stethoscope"></div><div class="badge"><svg width="12" height="12" viewBox="0 0 24 24" fill="#fff"><path d="M12 21s-8-5-8-11a4.5 4.5 0 0 1 8-3 4.5 4.5 0 0 1 8 3c0 6-8 11-8 11z"/></svg></div><h4>Peter Vance</h4><span>Neurology</span></div>
    <div class="doc"><div class="doc-photo" role="img" aria-label="Portrait of a pediatric doctor in a white coat"></div><div class="badge"><svg width="12" height="12" viewBox="0 0 24 24" fill="#fff"><path d="M12 21s-8-5-8-11a4.5 4.5 0 0 1 8-3 4.5 4.5 0 0 1 8 3c0 6-8 11-8 11z"/></svg></div><h4>Leo Tran</h4><span>Pediatric</span></div>
  </div>
</section>

<section class="news">
  <h2 class="section-title" style="top:58px">News &amp; Blog</h2>
  <p class="section-sub" style="top:101px">Donec quam felis, ultricies nec, pellentesque eu, pretium quis, sem. Nulla consequat massa quis enim. Donec pede justo, fringilla vel, aliquet nec.</p>
  <div class="posts">
    <article class="post"><div class="post-img" role="img" aria-label="Laboratory work with blue gloves and test tubes" style="background:linear-gradient(135deg,#e7f2fb,#7fb2e6 55%,#cfe3f5)"></div><div class="date"><b>30</b><small>Aug</small></div><div class="meta"><span>Admin</span><span>Uncategorized</span></div><h4>Dental doctors examine patients so that...</h4></article>
    <article class="post"><div class="post-img" role="img" aria-label="Surgical team working in an operating room" style="background:linear-gradient(135deg,#dfe9f3,#8fb4d8 50%,#5f8fc0)"></div><div class="date"><b>30</b><small>Aug</small></div><div class="meta"><span>Admin</span><span>Uncategorized</span></div><h4>Dental doctors examine patients so that...</h4></article>
    <article class="post"><div class="post-img" role="img" aria-label="Surgeons in scrubs during an operation" style="background:linear-gradient(135deg,#e3ecf4,#9dbfdc 50%,#6f9cc6)"></div><div class="date"><b>20</b><small>Aug</small></div><div class="meta"><span>Admin</span><span>Uncategorized</span></div><h4>Dental doctors examine patients so that...</h4></article>
  </div>
</section>

<section class="cta">
  <h3>SCHEDULE YOUR APPOINTMENT</h3>
  <a class="btn cta-btn">SCHEDULE NOW</a>
  <div class="call">CALL: +1 555 010 2048</div>
</section>

<footer class="footer">
  <div class="col" style="left:183px">
    <h4>About Us</h4>
    <div style="margin-top:8px">
      <div class="contact-row"><svg viewBox="0 0 24 24" fill="#33d1bf"><path d="M12 2a7 7 0 0 0-7 7c0 5 7 13 7 13s7-8 7-13a7 7 0 0 0-7-7zm0 9.5a2.5 2.5 0 1 1 0-5 2.5 2.5 0 0 1 0 5z"/></svg>48 Linden Avenue, Portland, OR</div>
      <div class="contact-row"><svg viewBox="0 0 24 24" fill="#33d1bf"><path d="M5 3h4l2 5-3 2a11 11 0 0 0 6 6l2-3 5 2v4a2 2 0 0 1-2 2A17 17 0 0 1 3 5a2 2 0 0 1 2-2z"/></svg>+1 555 010 2048</div>
      <div class="contact-row"><svg viewBox="0 0 24 24" fill="none" stroke="#33d1bf" stroke-width="2.4"><rect x="7" y="2" width="10" height="20" rx="2"/><path d="M11 18h2"/></svg>+1 555 010 2048</div>
      <div class="contact-row"><svg viewBox="0 0 24 24" fill="none" stroke="#33d1bf" stroke-width="2.2"><rect x="3" y="5" width="18" height="14" rx="1"/><path d="M3 6l9 7 9-7"/></svg>hello@maplecrest.com</div>
    </div>
    <div class="foot-social"><i></i><i></i><i></i></div>
  </div>
  <div class="col" style="left:468px">
    <h4>Services</h4>
    <ul class="svc-list">
      <li>Cosmetic Dentistry</li><li>Implants</li><li>Dental Hygiene</li><li>Emergency Services</li><li>Restorations</li><li>Dentures</li>
    </ul>
  </div>
  <div class="col hours" style="left:753px">
    <h4>Opening Hours</h4>
    <div style="margin-top:8px;font-size:10px">
      <div class="contact-row"><span><svg viewBox="0 0 24 24" fill="none" stroke="#33d1bf" stroke-width="2.4"><circle cx="12" cy="12" r="9"/><path d="M12 7v5l3 2"/></svg>Monday</span>8:00 AM - 9:00 PM</div>
      <div class="contact-row"><span><svg viewBox="0 0 24 24" fill="none" stroke="#33d1bf" stroke-width="2.4"><circle cx="12" cy="12" r="9"/><path d="M12 7v5l3 2"/></svg>Tuesday</span>8:00 AM - 9:00 PM</div>
      <div class="contact-row"><span><svg viewBox="0 0 24 24" fill="none" stroke="#33d1bf" stroke-width="2.4"><circle cx="12" cy="12" r="9"/><path d="M12 7v5l3 2"/></svg>Wednesday</span>8:00 AM - 9:00 PM</div>
      <div class="contact-row"><span><svg viewBox="0 0 24 24" fill="none" stroke="#33d1bf" stroke-width="2.4"><circle cx="12" cy="12" r="9"/><path d="M12 7v5l3 2"/></svg>Thursday</span>8:00 AM - 9:00 PM</div>
      <div class="contact-row"><span><svg viewBox="0 0 24 24" fill="none" stroke="#33d1bf" stroke-width="2.4"><circle cx="12" cy="12" r="9"/><path d="M12 7v5l3 2"/></svg>Friday</span>8:00 AM - 9:00 PM</div>
      <div class="contact-row"><span><svg viewBox="0 0 24 24" fill="none" stroke="#33d1bf" stroke-width="2.4"><circle cx="12" cy="12" r="9"/><path d="M12 7v5l3 2"/></svg>Saturday</span>9:00 AM - 6:00 PM</div>
      <div class="contact-row"><span><svg viewBox="0 0 24 24" fill="none" stroke="#33d1bf" stroke-width="2.4"><circle cx="12" cy="12" r="9"/><path d="M12 7v5l3 2"/></svg>Sunday</span>CLOSED</div>
    </div>
  </div>
</footer>
<div class="copy">Copyright © 2025 Maplecrest Dentistry. All Rights Reserved.</div>
<div class="totop"><svg width="14" height="10" viewBox="0 0 14 10" fill="#fff"><path d="M7 1l6 8H1z"/></svg></div>

</body>
</html>
```